Business Card design for a mini spa

business card for a small natural skincare/waxing spa. I need a modern, clean, classy card that draws people in but also need to be able to write future appointments on one side of it.

Target Market(s)

women age 16-70

Industry/Entity Type

Beauty Salon

Contact Information for Business Card

Fernlight Skin Care 907-318-2796
2958 W Talvenby Selvara, AK 99683
Facial, Waxing, Spray Tanning,

Colors
33b8a4

Requirements
Must have
• Fernlight logo with flower
• my tag line "quiet roots bright bloom"
• 907-318-2796
• 2958 W Talvenby
• a place to write ......Your Next Appointment
• Mira Oskenfeld
Nice to have
• something modern, elegant, clean and simple with my attached logo. I also attached a few pictures of what I like along with a color pallet and a few fonts that I like.
Should not have
• no pictures of people in a spa I do not want your typical spa pictures like stone, people receiving a treatment.

```html
<!DOCTYPE html>
<html lang="en">
<head>
<meta charset="utf-8">
<title>Fernlight Skin Care – Business Card</title>
<link href="https://fonts.googleapis.com/css2?family=Josefin+Sans:wght@200&family=Quattrocento+Sans&family=Quicksand:wght@400;500&display=swap" rel="stylesheet">
<style>
  :root {
    --backdrop: #929397;
    --teal: #72cacb;
    --teal-text: #5fc7c6;
    --gold: #c6b286;
    --cream: #efe6d2;
    --paper-light: #ffffff;
    --paper-edge: #d9dadb;
    --rule: #e3d6bc;
  }
  * { margin: 0; padding: 0; box-sizing: border-box; }
  html, body { width: 1200px; height: 1000px; overflow: hidden; }
  body { background: var(--backdrop); position: relative; font-family: "Quicksand", sans-serif; }

  .card {
    position: absolute; left: 318px; width: 565px; height: 330px; overflow: hidden;
    background: radial-gradient(ellipse at 40% 40%, var(--paper-light) 0%, #ececed 55%, var(--paper-edge) 100%);
    box-shadow: 4px 5px 6px rgba(0,0,0,0.35);
  }
  .card--front { top: 144px; }
  .card--back { top: 525px; height: 331px; }
  .card svg.shapes { position: absolute; inset: 0; }

  .decor {
    position: absolute;
    background: radial-gradient(circle, rgba(239,230,210,0.75) 0%, rgba(239,230,210,0.35) 55%, rgba(239,230,210,0) 75%);
  }
  .decor--top-right { left: 420px; top: -10px; width: 170px; height: 150px; }
  .decor--bottom-left { left: -30px; top: 170px; width: 200px; height: 180px; }

  .brand { position: absolute; left: 30px; top: 42px; width: 250px; text-align: center; }
  .brand__name {
    font-family: "Josefin Sans", sans-serif; font-weight: 200; font-size: 38px;
    color: var(--teal-text); letter-spacing: 1px; line-height: 1; text-transform: uppercase;
  }
  .brand__sub {
    font-family: "Quattrocento Sans", sans-serif; font-size: 20px; color: var(--gold);
    letter-spacing: 1.5px; margin-top: 22px; line-height: 1;
  }
  .brand__tagline { font-size: 16.5px; color: var(--teal-text); margin-top: 6px; line-height: 1; }

  .contact {
    position: absolute; left: 294px; top: 186px; width: 271px; height: 116px;
    background: rgba(255,255,255,0.35); border: 1px solid var(--rule); border-right: none;
  }
  .contact__title {
    height: 31px; padding: 6px 0 0 15px; font-size: 17px; color: var(--gold);
    border-bottom: 1px solid var(--rule);
  }
  .contact__lines { padding: 13px 0 0 15px; font-size: 12.5px; color: var(--teal-text); line-height: 20px; }
  .contact__services {
    position: absolute; left: -1px; right: 0; bottom: -1px; height: 26px; background: var(--gold);
    color: #fff; font-size: 12px; padding: 5px 0 0 15px;
  }

  .appointment__label {
    position: absolute; left: 32px; top: 26px; color: #fff; font-size: 19px; font-weight: 400;
  }
  .appointment__sheet {
    position: absolute; left: 31px; top: 52px; width: 369px; height: 254px;
    background: #fff; border: 1px solid #d8c9a6;
  }
  .appointment__line { position: absolute; left: 11px; right: 10px; height: 1px; background: var(--rule); }
  .brand-mark { position: absolute; left: 430px; top: 125px; width: 90px; text-align: center; color: #fff; }
  .brand-mark__dot { width: 44px; height: 44px; margin: 0 auto 8px; border: 2px solid #fff; border-radius: 50%; }
  .brand-mark__name { font-family: "Quattrocento Sans", sans-serif; font-size: 15px; letter-spacing: 1px; }
</style>
</head>
<body>

<section class="card card--front">
  <div class="decor decor--top-right" role="img" aria-label="Faint cream line-art flower decoration"></div>
  <div class="decor decor--bottom-left" role="img" aria-label="Faint cream line-art flower decoration"></div>
  <svg class="shapes" viewBox="0 0 565 330" width="565" height="330">
    <path d="M150,160 C260,165 350,140 440,140 C500,140 540,150 565,160 L565,170 C520,156 470,150 420,152 C330,157 250,172 150,160Z" fill="var(--teal)"/>
    <path d="M0,134 C110,168 200,178 300,162 C400,146 480,150 565,168 L565,185 C480,164 400,164 300,174 C200,184 110,172 0,140Z" fill="var(--gold)"/>
  </svg>
  <div class="brand">
    <div class="brand__name">Fernlight</div>
    <div class="brand__sub">SKIN CARE</div>
    <div class="brand__tagline">quiet roots bright bloom</div>
  </div>
  <div class="contact">
    <div class="contact__title">Fernlight Skin Care</div>
    <div class="contact__lines">
      907-318-2796<br>
      2958 W Talvenby Selvara, AK 99683
    </div>
    <div class="contact__services">Facial &nbsp;|&nbsp; Waxing &nbsp;|&nbsp; Spray Tanning</div>
  </div>
</section>

<section class="card card--back">
  <svg class="shapes" viewBox="0 0 565 331" width="565" height="331">
    <path d="M0,0 H565 V218 C510,262 450,282 395,285 L40,285 L40,75 C25,68 12,64 0,62Z" fill="var(--teal)"/>
    <path d="M0,62 C12,64 25,68 40,75 L40,92 C25,84 12,77 0,72Z" fill="var(--gold)"/>
    <path d="M565,218 C510,262 450,282 395,285 L395,292 C460,290 520,272 565,245Z" fill="var(--gold)"/>
    <path d="M375,47 L404,47 L404,78Z" fill="var(--gold)"/>
  </svg>
  <div class="appointment__label">Your Next Appointment</div>
  <div class="appointment__sheet">
    <div class="appointment__line" style="top:43px"></div>
    <div class="appointment__line" style="top:87px"></div>
    <div class="appointment__line" style="top:132px"></div>
    <div class="appointment__line" style="top:176px"></div>
    <div class="appointment__line" style="top:220px"></div>
  </div>
  <div class="brand-mark">
    <div class="brand-mark__dot"></div>
    <div class="brand-mark__name">Fernlight</div>
  </div>
</section>

</body>
</html>
```